Personal Training

The name of my company is Heron Fitness. I am looking for a design that will feature the 8 components I am utilizing in my workouts (strength, flexibility, agility, core, power, balance, cardiovacular, speed) and represent the spider. It is not essesstial to have a spider for my logo but would be nice. If a spider is used please do not use a logo like Gullwoman, a tarantula, or anything scary involving a spider (I have female clients who would get scared) lol
If you need me to provide more information please let me know. Feel free to check my website for ideas but ignore the pictures on my site as those are not pictures of me or clients
Thank you in advance!

Industry/Entity Type

Fitness

Contact Information for Business Card

Mark Delaney
Company Name: Heron Fitness
Tag line: 8 components to a better you
Website: hernfit4.example
Email: mark@hernfit4.example
Cell: 555-314-2086

CQBL Certified Personal Trainer
CPR AED National Pulse Federation
B.A. Exercise Physiology W.K.R., 2004

```html
<!DOCTYPE html>
<html lang="en">
<head>
<meta charset="utf-8">
<title>Heron Fitness – Business Card</title>
<link href="https://fonts.googleapis.com/css2?family=Roboto:wght@300;400;700&family=Allura&display=swap" rel="stylesheet">
<style>
  :root {
    --page-bg: #e9e6e1;
    --card-dark: #1c1c1d;
    --card-mid: #2d2d2f;
    --accent: #e8666a;
    --text-light: #e9e9e9;
    --text-soft: #bdbdbd;
    --web-tone: #3a3a3c;
  }
  * { margin: 0; padding: 0; box-sizing: border-box; }
  html, body {
    width: 1200px; height: 1024px; overflow: hidden;
    background: var(--page-bg);
    font-family: "Roboto", Arial, sans-serif;
  }
  .card {
    position: absolute; left: 75px; top: 212px;
    width: 1050px; height: 600px;
    background: radial-gradient(ellipse at 55% 40%, var(--card-mid) 0%, var(--card-dark) 75%);
    box-shadow: 0 20px 40px rgba(0,0,0,0.25);
    color: var(--text-light);
    overflow: hidden;
  }
  .web-decoration {
    position: absolute; left: 0; bottom: 0;
    width: 260px; height: 300px;
    background: radial-gradient(circle at 0% 100%, var(--web-tone) 0%, rgba(58,58,60,0.4) 50%, rgba(58,58,60,0) 75%);
  }
  .brand-name {
    position: absolute; left: 110px; top: 70px;
    font-weight: 700; font-size: 78px; letter-spacing: 2px;
    color: var(--accent); text-transform: uppercase; line-height: 1;
  }
  .tagline {
    position: absolute; left: 300px; top: 152px;
    font-family: "Allura", cursive; font-size: 40px; color: var(--text-light);
  }
  .rule {
    position: absolute; left: 350px; width: 460px; height: 1px;
    background: linear-gradient(90deg, rgba(232,102,106,0) 0%, var(--accent) 30%, var(--accent) 70%, rgba(232,102,106,0) 100%);
  }
  .rule--top { top: 222px; }
  .rule--bottom { top: 410px; }
  .trainer { position: absolute; left: 0; right: 0; top: 250px; text-align: center; padding-left: 120px; }
  .trainer-name { font-size: 34px; font-weight: 300; letter-spacing: 1px; text-transform: uppercase; }
  .trainer-name strong { font-weight: 700; }
  .credentials { margin-top: 14px; font-size: 20px; font-weight: 300; color: var(--text-soft); line-height: 1.5; }
  .contact-row {
    position: absolute; left: 250px; right: 60px; bottom: 70px;
    display: flex; justify-content: space-between; align-items: center;
    font-size: 20px;
  }
  .contact-item { display: flex; align-items: center; gap: 10px; }
  .contact-item svg { width: 18px; height: 18px; fill: var(--accent); }
  .contact-item--phone { font-weight: 700; }
</style>
</head>
<body>
  <div class="card">
    <div class="web-decoration" role="img" aria-label="Faint spider web decoration in the corner"></div>

    <div class="brand-name">Heron Fitness</div>
    <div class="tagline">8 components to a better you</div>

    <div class="rule rule--top"></div>
    <div class="trainer">
      <div class="trainer-name"><strong>Mark</strong> Delaney</div>
      <div class="credentials">
        CQBL Certified Personal Trainer CPR AED<br>
        National Pulse Federation B.A. Exercise Physiology W.K.R., 2004
      </div>
    </div>
    <div class="rule rule--bottom"></div>

    <div class="contact-row">
      <div class="contact-item contact-item--phone">
        <svg viewBox="0 0 24 24" aria-hidden="true"><path d="M6.6 10.8a15 15 0 0 0 6.6 6.6l2.2-2.2a1 1 0 0 1 1-.25 11.4 11.4 0 0 0 3.6.57 1 1 0 0 1 1 1V20a1 1 0 0 1-1 1A17 17 0 0 1 3 4a1 1 0 0 1 1-1h3.5a1 1 0 0 1 1 1c0 1.25.2 2.45.57 3.57a1 1 0 0 1-.25 1z"/></svg>
        <span>555 314 2086</span>
      </div>
      <div class="contact-item">
        <svg viewBox="0 0 24 24" aria-hidden="true"><path d="M3 5h18v14H3z M4 6.5v.3l8 5.2 8-5.2v-.3z" fill-rule="evenodd"/></svg>
        <span>mark@hernfit4.example</span>
      </div>
      <div class="contact-item">
        <svg viewBox="0 0 24 24" aria-hidden="true"><circle cx="12" cy="12" r="10"/><path d="M2 12h20M12 2c3 3 3 17 0 20M12 2c-3 3-3 17 0 20" stroke="#1c1c1d" stroke-width="1.4" fill="none"/></svg>
        <span>www.hernfit4.example</span>
      </div>
    </div>
  </div>
</body>
</html>
```